Business card for home developer

Name, email, phone #, logo, address, lic # and slogan.
Slogan to say something like, "Leader in quality neighborhood communities" maybe? The last one said "A sept above the rest". Some thing saying we are above the other people.
Updates
The card can be two sided?
Target Market(s)
Home buyers
Industry/Entity Type
Business
Look and feel
Each slider illustrates characteristics of the customer's brand and the style your logo design should communicate.

```html
<!DOCTYPE html>
<html lang="en">
<head>
<meta charset="utf-8">
<title>Summitline Homes – Business Card</title>
<link href="https://fonts.googleapis.com/css2?family=Montserrat:wght@400;500;800&display=swap" rel="stylesheet">
<style>
  :root {
    --navy: #264783;
    --red: #a52127;
    --white: #ffffff;
    --page: #ffffff;
  }
  html, body {
    margin: 0;
    padding: 0;
    width: 1200px;
    height: 900px;
    overflow: hidden;
    background: var(--page);
    font-family: "Montserrat", sans-serif;
  }
  .business-card {
    position: absolute;
    left: 72px;
    top: 136px;
    width: 1055px;
    height: 645px;
    background: var(--white);
    overflow: hidden;
  }
  .sweep {
    position: absolute;
    inset: 0;
  }
  .slogan {
    position: absolute;
    left: 88px;
    top: 30px;
    margin: 0;
    font-size: 30px;
    font-weight: 500;
    color: var(--white);
    text-shadow: 0 0 3px rgba(0,0,0,0.85), 1px 1px 4px rgba(0,0,0,0.6);
    letter-spacing: 0.2px;
  }
  .brand {
    position: absolute;
    right: 45px;
    top: 56px;
    display: flex;
    align-items: center;
    gap: 16px;
  }
  .brand-name {
    margin: 0;
    color: var(--navy);
    font-weight: 800;
    font-size: 68px;
    line-height: 0.95;
    text-transform: uppercase;
    text-align: right;
    letter-spacing: -1px;
  }
  .brand-mark {
    width: 70px;
    height: 70px;
    border-radius: 50%;
    border: 3px solid var(--navy);
    box-sizing: border-box;
    align-self: flex-start;
    margin-top: -4px;
  }
  .contact {
    position: absolute;
    right: 49px;
    top: 318px;
    margin: 0;
    padding: 0;
    list-style: none;
    text-align: right;
    font-size: 39px;
    font-weight: 400;
    line-height: 50px;
  }
  .contact .accent { color: var(--red); }
  .contact .primary { color: var(--navy); }
  .holder-name {
    position: absolute;
    left: 36px;
    top: 556px;
    margin: 0;
    color: var(--white);
    font-size: 52px;
    font-weight: 400;
  }
</style>
</head>
<body>
  <section class="business-card">
    <svg class="sweep" viewBox="0 0 1055 645" width="1055" height="645" aria-hidden="true">
      <path d="M0 0 L13 0 C 120 380, 520 590, 1055 636 L1055 645 L0 645 Z" fill="var(--navy)"/>
    </svg>

    <p class="slogan">Where dreams are built</p>

    <div class="brand">
      <h1 class="brand-name">Summitline<br>Homes</h1>
      <span class="brand-mark"></span>
    </div>

    <ul class="contact">
      <li class="accent">Nhart@Summitline.com</li>
      <li class="primary">Licence No: 51872</li>
      <li class="accent">24 Ridge Lane</li>
      <li class="primary">5550 1234</li>
    </ul>

    <p class="holder-name">Nolan Hart</p>
  </section>
</body>
</html>
```